Business Card design for construction company

I would like a business card design for a construction company - Harlow Constructions. I have attached the ai logo file for use. I would like the card to be very smart and clean and incorporate only white and the two colours in the logo. I would like the card to have two sides. One side can just have the logo, the other with the relevant information.

Target Market(s)

Building and Construction Clients

Industry/Entity Type

Business

Contact Information for Business Card

Name: Tom Pardoe
Company: Harlow Constructions Pty Limited
Address: 14 Mallee Crescent Carrow Vale 2093
Phone: 0427 531 068
Email: tomp@harlowbuild-example.com.au

Font styles to use
Serif
Sans Serif

Requirements
Must have
• Details noted above
• Logo as provided
• Colours as in logo
• Square edges
• A font that compliments the logo
Should not have
• Any colour other than white and those in logo
• Rounded edges

```html
<!DOCTYPE html>
<html lang="en">
<head>
<meta charset="utf-8">
<title>Harlow Constructions – Business Card</title>
<link href="https://fonts.googleapis.com/css2?family=Lato:wght@400&display=swap" rel="stylesheet">
<style>
  :root {
    --backdrop: #e9e7e3;
    --band-dark: #1f1e1f;
    --band-light: #3a3836;
    --accent-blue: #1aa6e0;
    --paper: #ffffff;
    --paper-shade: #eeeeef;
    --ink-grey: #555558;
    --ink-soft: #6a6a6e;
  }
  * { box-sizing: border-box; margin: 0; padding: 0; }
  html, body {
    width: 1200px; height: 797px; overflow: hidden;
    background: var(--backdrop);
  }
  .sheet {
    position: relative; width: 1200px; height: 797px;
    display: flex; align-items: center; justify-content: center; gap: 60px;
  }
  .card {
    position: relative; width: 520px; height: 300px;
    background: linear-gradient(180deg, var(--paper) 40%, var(--paper-shade) 100%);
    overflow: hidden;
    box-shadow: 0 10px 24px rgba(0,0,0,0.18);
  }
  .band { position: absolute; left: 0; right: 0; background: var(--band-dark); }
  .band--top {
    top: 0; height: 40px;
    background: linear-gradient(180deg, var(--band-light), var(--band-dark));
  }
  .band--bottom { bottom: 0; height: 58px; }
  .band__line {
    position: absolute; left: 8%; right: 8%; height: 2px;
    background: linear-gradient(90deg, transparent, var(--accent-blue) 30%, var(--accent-blue) 70%, transparent);
  }
  .band--top .band__line { bottom: 6px; }
  .band--bottom .band__line { top: 6px; }

  .company-name {
    font-family: "Lato", sans-serif;
    font-weight: 400;
    color: var(--ink-grey);
    letter-spacing: 0.08em;
    white-space: nowrap;
  }
  .card--front .company-name {
    position: absolute; left: 0; right: 0; top: 146px;
    text-align: center; font-size: 22px;
  }
  .card--back .company-name {
    position: absolute; left: 26px; top: 174px; font-size: 13px;
  }
  .swoosh { position: absolute; left: 236px; top: 40px; width: 70px; height: 202px; }

  .contact {
    position: absolute; left: 300px; top: 86px;
    font-family: "Lato", sans-serif; font-size: 12.5px; color: var(--ink-soft);
    line-height: 1.45; list-style: none;
  }
  .contact__item { display: flex; align-items: flex-start; gap: 7px; }
  .contact__item--address { margin-bottom: 12px; }
  .contact__icon { width: 11px; height: 11px; margin-top: 3px; flex: none; fill: var(--accent-blue); }
</style>
</head>
<body>
<main class="sheet">
  <section class="card card--front" aria-label="Card front">
    <div class="band band--top"><span class="band__line"></span></div>
    <p class="company-name">Harlow Constructions</p>
    <div class="band band--bottom"><span class="band__line"></span></div>
  </section>

  <section class="card card--back" aria-label="Card back">
    <div class="band band--top"><span class="band__line"></span></div>
    <p class="company-name">Harlow Constructions</p>
    <svg class="swoosh" viewBox="0 0 70 202" aria-hidden="true">
      <defs>
        <linearGradient id="swooshShade" x1="0" x2="1">
          <stop offset="0" stop-color="#c9c9cc"/>
          <stop offset="1" stop-color="#ffffff" stop-opacity="0"/>
        </linearGradient>
      </defs>
      <path d="M4 0 Q50 100 60 202 L70 202 Q40 90 4 0 Z" fill="url(#swooshShade)"/>
    </svg>
    <ul class="contact">
      <li class="contact__item contact__item--address">
        <svg class="contact__icon" viewBox="0 0 12 12"><path d="M6 0a4 4 0 0 0-4 4c0 3 4 8 4 8s4-5 4-8a4 4 0 0 0-4-4zm0 5.6a1.6 1.6 0 1 1 0-3.2 1.6 1.6 0 0 1 0 3.2z"/></svg>
        <span>Address Line 1<br>Address Line 2</span>
      </li>
      <li class="contact__item">
        <svg class="contact__icon" viewBox="0 0 12 12"><path d="M2.5 0.5l2 2.5-1.2 1.5a7 7 0 0 0 4.2 4.2L9 7.5l2.5 2-1.3 2C5 11.5 0.5 7 0.5 1.8z"/></svg>
        <span>123 456 789</span>
      </li>
      <li class="contact__item">
        <svg class="contact__icon" viewBox="0 0 12 12"><circle cx="6" cy="6" r="5.2" fill="none" stroke="#1aa6e0" stroke-width="1.2"/><path d="M0.8 6h10.4M6 0.8c-3 3-3 7.4 0 10.4M6 0.8c3 3 3 7.4 0 10.4" fill="none" stroke="#1aa6e0" stroke-width="1"/></svg>
        <span>www.harlow-example.com</span>
      </li>
      <li class="contact__item">
        <svg class="contact__icon" viewBox="0 0 12 12"><path d="M0.5 2h11v8h-11z" fill="none" stroke="#1aa6e0" stroke-width="1.2"/><path d="M0.5 2L6 6.5 11.5 2" fill="none" stroke="#1aa6e0" stroke-width="1.2"/></svg>
        <span>smith@harlow-example.com</span>
      </li>
    </ul>
    <div class="band band--bottom"><span class="band__line"></span></div>
  </section>
</main>
</body>
</html>
```